Lantern Petro - needs a business card

Lantern Petro is a U.S. based diesel sourcing and distribution company that supports American oil & gas fields through providing quality product and consistent services.

Target Market(s)

Oil and Gas

Contact Information for Business Card

The background of the card must be white to ensure the logo pops.

Font styles to use
Serif
Sans Serif

Colors

Designer to choose colors to be used in the design.

Requirements
Must have
• Front of Card: Tag line: Lantern Petro, Powering the Nation's Oil & Gas fields.
• Not sure if you guys do this part but just in case...
• Dale Winterholt
• Owner/CEO
• C:701.555.0148
• E:Dwinterholt@lanternpetro.com
• W:Lanternpetro.com
• Locations: Servicing the Powder River, DJ basin and Bakken formations.
• Back of Card: " Frac fueling is what we do. We understand how important diesel fuel is to your operation, which is why our main service line is Frac fueling. We assure our supply and stand by our service"

```html
<!DOCTYPE html>
<html lang="en">
<head>
<meta charset="utf-8">
<title>Lantern Petro – Business Card</title>
<link href="https://fonts.googleapis.com/css2?family=Source+Serif+4:wght@400;600;700&display=swap" rel="stylesheet">
<style>
  :root {
    --page: #e9e7e4;
    --card: #ffffff;
    --ink: #1f2a44;
    --ink-soft: #2e3a55;
    --accent: #c8202f;
    --rule: #1f2a44;
    --serif: "Source Serif 4", Georgia, serif;
  }
  * { margin: 0; padding: 0; box-sizing: border-box; }
  html, body { width: 792px; height: 1200px; overflow: hidden; }
  body {
    background: var(--page);
    font-family: var(--serif);
    color: var(--ink);
    position: relative;
  }
  .card {
    position: absolute;
    left: 76px;
    width: 640px;
    height: 366px;
    background: var(--card);
    box-shadow: 0 2px 10px rgba(0,0,0,0.08);
  }
  .card--front { top: 180px; }
  .card--back  { top: 650px; }

  /* Front */
  .brand {
    position: absolute;
    left: 56px;
    top: 44px;
    display: flex;
    align-items: center;
    gap: 8px;
    font-size: 15px;
    font-weight: 600;
    color: var(--ink);
  }
  .brand__dot {
    width: 12px; height: 12px;
    border-radius: 50%;
    background: var(--accent);
  }
  .person {
    position: absolute;
    left: 56px;
    top: 140px;
    font-size: 30px;
    line-height: 1.2;
    color: var(--ink);
  }
  .person__last { font-weight: 700; display: block; }
  .person__first, .person__title { font-weight: 400; display: block; }
  .divider {
    position: absolute;
    left: 236px;
    top: 40px;
    width: 2px;
    height: 268px;
    background: var(--rule);
  }
  .details {
    position: absolute;
    left: 262px;
    top: 42px;
    list-style: none;
    font-size: 14px;
    line-height: 1.25;
    color: var(--ink-soft);
  }
  .details li { margin-bottom: 13px; }
  .details li.tight { margin-bottom: 4px; }

  /* Back */
  .quote {
    position: absolute;
    inset: 0;
    display: flex;
    align-items: center;
    justify-content: center;
    padding: 0 70px;
    text-align: center;
    font-size: 23px;
    line-height: 1.25;
    color: var(--ink);
  }
</style>
</head>
<body>
  <section class="card card--front" aria-label="Business card front">
    <div class="brand"><span class="brand__dot"></span>Lantern Petro</div>
    <p class="person">
      <span class="person__first">Dale</span>
      <span class="person__last">Winterholt</span>
      <span class="person__title">Owner</span>
    </p>
    <div class="divider"></div>
    <ul class="details">
      <li>Lantern Petro</li>
      <li>Powering the Nation's Oil &amp; Gas fields</li>
      <li class="tight">Servicing the Powder River, DJ basin</li>
      <li>and Bakken formations</li>
      <li>C:701.555.0148</li>
      <li>Dwinterholt@lanternpetro.com</li>
      <li>Lanternpetro.com</li>
    </ul>
  </section>

  <section class="card card--back" aria-label="Business card back">
    <p class="quote">"Frac fueling is what we do. We understand how important diesel fuel is to your operation, which is why our main service line is Frac fueling. We assure our supply and stand by our service"</p>
  </section>
</body>
</html>
```